Business Card Design Project

I am opening a skin care studio called Glow Bloom by Marisa. I will be offering a wide range of unique and affordable skin services including facials, chemical peels, microdermabrasion treatments, body wraps, salt glows, all waxing and eye lash extensions. If the business cards depicts what I would like, this would lead to brochures, web design, signs, etc.
Updates

Project Deadline Extended
Reason: A request to extend deadline was requested. I will be more than happy to accommodate.

Industry/Entity Type

Business

Requirements
Nice to have
• facial features so prospective client clearly identifies what type of business this is. Not stuffy or boring "spa" looking graphics. I am focusing just on face, body, waxing, eyelashes. No massage or nails.

```html
<!DOCTYPE html>
<html lang="en">
<head>
<meta charset="utf-8">
<title>Glow Bloom by Marisa – Business Cards</title>
<link rel="stylesheet" href="https://fonts.googleapis.com/css2?family=Alegreya:wght@700&family=Open+Sans:wght@400;600&display=swap">
<style>
  :root {
    --backdrop: #ece7e1;
    --purple: #5c2f7c;
    --purple-deep: #4a2266;
    --purple-light: #8a55a8;
    --lime: #a4c62c;
    --lime-deep: #7f9d25;
    --white: #ffffff;
    --paper: #f3f3f5;
  }
  * { margin: 0; padding: 0; box-sizing: border-box; }
  html, body { width: 1200px; height: 900px; overflow: hidden; }
  body {
    background: var(--backdrop);
    display: flex;
    align-items: center;
    justify-content: center;
    gap: 40px;
  }
  .card {
    position: relative;
    width: 540px;
    height: 310px;
    border-radius: 4px;
    overflow: hidden;
    box-shadow: 0 6px 18px rgba(60, 40, 70, 0.25);
  }
  .card-art { position: absolute; inset: 0; width: 100%; height: 100%; }
  .brand-name {
    position: absolute;
    font-family: "Alegreya", Georgia, serif;
    font-weight: 700;
    color: var(--lime);
    line-height: 1;
    white-space: nowrap;
  }
  /* Front */
  .card-front .brand-name { top: 26px; left: 150px; font-size: 36px; }
  .contact {
    position: absolute;
    left: 34px;
    bottom: 22px;
    color: var(--white);
    font-family: "Alegreya", Georgia, serif;
    font-weight: 700;
    line-height: 1.25;
  }
  .contact-name { font-size: 24px; }
  .contact-role { font-size: 15px; margin-bottom: 8px; }
  .contact-line { font-size: 16px; }
  /* Back */
  .card-back .brand-name { top: 62px; right: 34px; font-size: 36px; }
  .services {
    position: absolute;
    top: 118px;
    right: 34px;
    text-align: right;
    color: var(--white);
    font-family: "Open Sans", Arial, sans-serif;
    font-size: 13px;
    line-height: 1.45;
  }
  .services span::before { content: "• "; }
  .services span + span { margin-left: 10px; }
  .website {
    position: absolute;
    top: 204px;
    left: 150px;
    color: var(--white);
    font-family: "Open Sans", Arial, sans-serif;
    font-weight: 600;
    font-size: 15px;
    transform: rotate(14deg);
    transform-origin: left center;
  }
</style>
</head>
<body>

<section class="card card-front" aria-label="Business card front">
  <svg class="card-art" viewBox="0 0 540 310" preserveAspectRatio="none" aria-hidden="true">
    <defs>
      <linearGradient id="front-paper" x1="0" y1="0" x2="1" y2="1">
        <stop offset="0" stop-color="#ffffff"/>
        <stop offset="1" stop-color="#e6e6ea"/>
      </linearGradient>
      <radialGradient id="front-purple" cx="0.35" cy="0.7" r="0.8">
        <stop offset="0" stop-color="#7a46a0"/>
        <stop offset="1" stop-color="#4e2570"/>
      </radialGradient>
    </defs>
    <rect width="540" height="310" fill="url(#front-purple)"/>
    <path d="M0 0 H540 V275 C420 240 250 150 0 75 Z" fill="var(--lime)"/>
    <path d="M0 0 H540 V262 C410 225 240 135 0 58 Z" fill="url(#front-paper)"/>
  </svg>
  <div class="brand-name">Glow Bloom by Marisa</div>
  <div class="contact">
    <div class="contact-name">Marisa Delvane</div>
    <div class="contact-role">Licensed Esthetician</div>
    <div class="contact-line">218 Alder Avenue Fairview, CO 80642</div>
    <div class="contact-line">555-014-2297</div>
  </div>
</section>

<section class="card card-back" aria-label="Business card back">
  <svg class="card-art" viewBox="0 0 540 310" preserveAspectRatio="none" aria-hidden="true">
    <defs>
      <radialGradient id="back-purple" cx="0.6" cy="0.45" r="0.7">
        <stop offset="0" stop-color="#8a55a8"/>
        <stop offset="1" stop-color="#55297a"/>
      </radialGradient>
      <linearGradient id="back-lime" x1="0" y1="0" x2="1" y2="1">
        <stop offset="0" stop-color="#a8c936"/>
        <stop offset="1" stop-color="#7f9d25"/>
      </linearGradient>
    </defs>
    <rect width="540" height="310" fill="url(#back-purple)"/>
    <path d="M0 60 C180 130 360 230 540 290 V310 H0 Z" fill="var(--purple-light)" opacity="0.55"/>
    <path d="M0 98 C190 170 370 255 540 300 V310 H0 Z" fill="url(#back-lime)"/>
  </svg>
  <div class="brand-name">Glow Bloom by Marisa</div>
  <div class="services">
    <div><span>body wraps</span><span>salt glows</span><span>facials</span></div>
    <div><span>chemical peels</span><span>microdermabrasion treatments</span></div>
  </div>
  <div class="website">www.glowbloombymarisa.com</div>
</section>

</body>
</html>
```